Quellbyte Business cards template

We're looking for something modern and elegant. We are a reseller of technology (computers, datacenter, etc). Color theme would be "only" white with the incorporation of the blue that's present on our website (Quellbyte.com) and logo file. We would like for the card to provide all the necessary info for the specific person (Phone#, fax#, email, name, website URL) . I'm attaching the logo file to this request. Please have it show Portland/Chicago somewhere, without providing specific addresses.

Target Market(s)

All b2b

Industry/Entity Type

Business

Contact Information for Business Card

Please have the color scheme be represented by only the white and blue from our website (Quellbyte.com) and logo. We would like to logo on the card, but not big and overwhelming. This card will be used as a template for anybody within the company, it should display the user's name, phone#, fax#, email, job title and website URL. Please have it show Portland/Chicago somewhere, without providing our specific addresses. Really, we're looking for a clean, simple and elegant look.

Font styles to use
Serif

Requirements
Must have
• Please see card details
Nice to have
• Please see card details
Should not have
• Anything tacky or tagline.

```html
<!DOCTYPE html>
<html lang="en">
<head>
<meta charset="utf-8">
<title>Quellbyte Business Card</title>
<link href="https://fonts.googleapis.com/css2?family=Quicksand:wght@400;500;600&family=Open+Sans:ital,wght@0,400;0,600;1,400&display=swap" rel="stylesheet">
<style>
  :root {
    --blue: #0c6fc1;
    --blue-deep: #0a5aa6;
    --blue-light: #3aa1e6;
    --white: #ffffff;
    --ink: #3b3f45;
    --stage: #e9ecef;
  }
  * { box-sizing: border-box; margin: 0; padding: 0; }
  html, body {
    width: 1200px; height: 1024px; overflow: hidden;
    background: var(--stage);
  }
  .card {
    position: absolute;
    left: 200px;
    width: 800px; height: 457px;
    border-radius: 4px;
    overflow: hidden;
    box-shadow: 0 6px 18px rgba(0,0,0,0.18);
  }
  .card-front { top: 40px; background: var(--white); }
  .card-back {
    top: 527px;
    background: linear-gradient(135deg, var(--blue-light) 0%, var(--blue) 45%, var(--blue-deep) 100%);
  }
  .swoosh { position: absolute; inset: 0; width: 100%; height: 100%; }
  .brand {
    position: absolute;
    font-family: "Quicksand", sans-serif;
    font-weight: 500;
    letter-spacing: 1px;
    white-space: nowrap;
  }
  .card-front .brand { left: 250px; top: 190px; font-size: 56px; line-height: 1; color: var(--blue); }
  .person { position: absolute; left: 265px; top: 268px; font-family: "Quicksand", sans-serif; }
  .person-name { font-size: 28px; font-weight: 600; color: var(--blue); line-height: 1.2; }
  .person-title { font-size: 16px; color: var(--blue-light); line-height: 1.3; }
  .contact-list {
    list-style: none;
    font-family: "Open Sans", sans-serif;
    font-size: 18px;
    color: var(--ink);
    letter-spacing: 0.5px;
    white-space: nowrap;
  }
  .contact-list li { display: flex; align-items: center; gap: 10px; height: 30px; }
  .contact-list svg { width: 15px; height: 15px; fill: var(--blue); flex: none; }
  .phones { position: absolute; left: 290px; top: 340px; }
  .details { position: absolute; left: 560px; top: 190px; font-size: 16px; }
  .card-back .brand {
    left: 0; right: 0; top: 170px; text-align: center;
    font-size: 88px; color: var(--white);
  }
  .back-url {
    position: absolute; left: 170px; top: 300px;
    font-family: "Open Sans", sans-serif; font-style: italic;
    font-size: 18px; color: var(--white); letter-spacing: 0.5px;
  }
</style>
</head>
<body>

<section class="card card-front">
  <svg class="swoosh" viewBox="0 0 800 457" preserveAspectRatio="none" aria-hidden="true">
    <path d="M0 0 H720 C520 40 250 110 0 230 Z" fill="var(--blue)"/>
    <path d="M0 246 C250 126 520 52 760 0 H790 C540 66 265 150 0 292 Z" fill="var(--blue-light)"/>
  </svg>

  <div class="brand">Quellbyte</div>

  <div class="person">
    <div class="person-name">Daniel Marsh</div>
    <div class="person-title">Managing Director</div>
  </div>

  <ul class="contact-list phones">
    <li><svg viewBox="0 0 16 16"><path d="M3 1h3l1.5 4-2 1.5a9 9 0 0 0 4 4L11 8.5l4 1.5v3a2 2 0 0 1-2 2A12 12 0 0 1 1 3a2 2 0 0 1 2-2z"/></svg>(555) 204-1180</li>
    <li><svg viewBox="0 0 16 16"><rect x="3" y="2" width="10" height="12" rx="1.5" fill="none" stroke="var(--blue)" stroke-width="1.6"/></svg>(555) 204-1181</li>
    <li><svg viewBox="0 0 16 16"><rect x="1" y="6" width="14" height="7" rx="1"/><rect x="4" y="2" width="8" height="4"/></svg>(555) 318-4426</li>
  </ul>

  <ul class="contact-list details">
    <li><svg viewBox="0 0 16 16"><rect x="1" y="3" width="14" height="10" rx="1"/><path d="M1.5 3.5 8 9l6.5-5.5" fill="none" stroke="#fff" stroke-width="1.2"/></svg>name@Quellbyte.com</li>
    <li><svg viewBox="0 0 16 16"><circle cx="8" cy="8" r="7"/><path d="M1 8h14M8 1c-3 3-3 11 0 14M8 1c3 3 3 11 0 14" fill="none" stroke="#fff" stroke-width="1"/></svg>www.Quellbyte.com</li>
    <li><svg viewBox="0 0 16 16"><path d="M8 1a5 5 0 0 1 5 5c0 4-5 9-5 9S3 10 3 6a5 5 0 0 1 5-5z"/><circle cx="8" cy="6" r="2" fill="#fff"/></svg>Portland/Chicago</li>
  </ul>
</section>

<section class="card card-back">
  <div class="brand">Quellbyte</div>
  <div class="back-url">www.Quellbyte.com</div>
</section>

</body>
</html>
```